Bright Path Therapies business cards and stationary

Need business cards and stationary designed to match previously made logo for for a new company based in Sydney NSW called 'Bright Path Therapies'.

We provide early intervention services and diagnostic assessment for children with disability and their families. I would like designs that are colourful and child friendly - possibly using feet/footprints/steps on a white background. The final design should communicate that we are family friendly, accepting and fun to work with.

Target Market(s)

Parents and Families
Teachers
Allied Health Professionals

Industry/Entity Type

Psychology

Contact Information for Business Card

Bright Path Therapies
www.brightpaththerapies.example
info@brightpaththerapies.example

Font styles to use
Sans Serif
Decorative
Script

Requirements
Must have
• Match the font and colour scheme of logo, along with footprint picture
Nice to have
• Clean and simple, while reflecting that I am working with families.
• Also- editable for when we make staff specific cards.

```html
<!DOCTYPE html>
<html lang="en">
<head>
<meta charset="utf-8">
<title>Bright Path Therapies – Business Card</title>
<link rel="stylesheet" href="https://fonts.googleapis.com/css2?family=Arimo:wght@400;700&display=swap">
<style>
  :root {
    --blue: #1f78c1;
    --green: #8cc63f;
    --orange: #f7941d;
    --red: #ef4136;
    --ink: #555a5f;
    --rule: #cfcfcf;
    --paper: #ffffff;
    --backdrop: #e6e6e6;
  }
  * { box-sizing: border-box; margin: 0; padding: 0; }
  html, body {
    width: 1200px;
    height: 1000px;
    overflow: hidden;
    background: var(--backdrop);
    font-family: "Arimo", Arial, sans-serif;
  }
  .card {
    position: absolute;
    left: 270px;
    width: 661px;
    height: 379px;
    background: var(--paper);
    box-shadow: 0 2px 6px rgba(0,0,0,0.25);
    overflow: hidden;
  }
  .card--front { top: 108px; }
  .card--back { top: 521px; }

  .footprint-pattern {
    position: absolute;
    inset: 0;
    background: linear-gradient(90deg,
      var(--blue) 0%, var(--blue) 16%,
      var(--green) 18%, var(--green) 32%,
      var(--orange) 34%, var(--orange) 48%,
      var(--red) 50%, var(--red) 64%,
      var(--blue) 66%, var(--blue) 82%,
      var(--green) 84%, var(--green) 100%);
    opacity: 0.85;
  }

  .brand {
    position: absolute;
    top: 60px;
    left: 0;
    right: 0;
    display: flex;
    align-items: center;
    justify-content: center;
    gap: 18px;
  }
  .brand__dot {
    width: 64px;
    height: 64px;
    border-radius: 50%;
    background: var(--red);
  }
  .brand__name {
    font-size: 38px;
    font-weight: 400;
    color: var(--blue);
    letter-spacing: 0.5px;
  }

  .staff {
    position: absolute;
    top: 224px;
    left: 60px;
    width: 243px;
    text-align: right;
  }
  .staff__name {
    font-size: 20px;
    font-weight: 700;
    color: var(--red);
    letter-spacing: 0.3px;
  }
  .staff__role {
    margin-top: 6px;
    font-size: 14px;
    color: var(--ink);
  }
  .divider {
    position: absolute;
    top: 221px;
    left: 328px;
    width: 1px;
    height: 50px;
    background: var(--rule);
  }
  .contact {
    position: absolute;
    top: 216px;
    left: 356px;
    list-style: none;
    font-size: 14.5px;
    color: var(--ink);
  }
  .contact li {
    display: flex;
    align-items: center;
    gap: 5px;
    height: 19.5px;
  }
  .contact svg { width: 11px; height: 11px; flex: none; }

  .hills {
    position: absolute;
    left: 0;
    bottom: 0;
    width: 661px;
    height: 56px;
  }
</style>
</head>
<body>
  <section class="card card--front">
    <div class="footprint-pattern" role="img" aria-label="Repeating pattern of colourful footprints in blue, green, orange and red columns"></div>
  </section>

  <section class="card card--back">
    <div class="brand">
      <span class="brand__dot"></span>
      <span class="brand__name">Bright Path Therapies</span>
    </div>

    <div class="staff">
      <p class="staff__name">MAREN HOLLOWAY</p>
      <p class="staff__role">Managing Director</p>
    </div>

    <div class="divider"></div>

    <ul class="contact">
      <li>
        <svg viewBox="0 0 12 12"><path d="M2.5 1 L4.5 1 L5 3.5 L3.8 4.5 Q5 7 7.5 8.2 L8.5 7 L11 7.5 L11 9.5 Q11 11 9.5 11 Q1 10 1 2.5 Q1 1 2.5 1 Z" fill="var(--blue)"/></svg>
        012-555-0147
      </li>
      <li>
        <svg viewBox="0 0 12 12"><rect x="0.5" y="2" width="11" height="8" fill="var(--orange)"/><path d="M0.5 2 L6 6.5 L11.5 2" fill="none" stroke="#fff" stroke-width="1"/></svg>
        info@brightpaththerapies.example
      </li>
      <li>
        <svg viewBox="0 0 12 12"><circle cx="6" cy="6" r="5.5" fill="var(--green)"/><path d="M0.5 6 H11.5 M6 0.5 V11.5 M6 0.5 Q2.5 6 6 11.5 M6 0.5 Q9.5 6 6 11.5" fill="none" stroke="#fff" stroke-width="0.7"/></svg>
        www.brightpaththerapies.example
      </li>
    </ul>

    <svg class="hills" viewBox="0 0 661 56" aria-hidden="true">
      <path d="M0 56 Q20 12 60 12 Q95 12 145 56 Z" fill="var(--blue)"/>
      <path d="M175 56 Q198 12 238 12 Q275 12 320 56 Z" fill="var(--red)"/>
      <path d="M350 56 Q373 12 413 12 Q450 12 495 56 Z" fill="var(--orange)"/>
      <path d="M522 56 Q545 12 585 12 Q622 12 661 50 L661 56 Z" fill="var(--green)"/>
    </svg>
  </section>
</body>
</html>
```